Need a clean & modern homepage for an education site + opportunity for longer term work

Thanks for viewing our project. We are excited about this new website and we hope that we might build a relationship with designers as we work on this project. I provided quite a few details and requirements to help you more quickly create a design that meets our needs.
Who we are:
We are a website that discusses the importance of college accreditation and provides a directory of college programs.
What we need:
A homepage that meets the below requirements and is inspired by the examples provided
Definition of accredited:
ac·cred·it·ed [uh-kred-i-tid] adj.
1. officially recognized as meeting the essential requirements, as of academic excellence: accredited schools.
2. provided with official credentials, as by a government: an accredited diplomatic representative.
3. accepted as authoritative: an accredited theory.
Overall look and feel for the homepage:
- Clean, simple and modern
- Limited (or zero) pictures
- Utilize color blocks with text
- A trend seems to be longer vertical length homepages with lots of whitespace. I generally like this trend as long as the page is not way to tall.
Inspirations: Sites that have a similar look and feel to what I need.
http://lernvista.org/
http://www.campusmetrix.com/colleges/orlen-university/
http://quietmarrow.org/
http://www.velmoratalent.com/
http://www.pluvo.com/
http://sketches.zumo.com/
Items to be included on the homepage. Details below on each item.
- Top navigation
- Logo: Please leave a blank area for a logo. The logo has not been designed.
- Simple graphic/color block at the top that highlights a definition of “Accredited” – the definition should be formatted like it is being copy/pasted from a dictionary.
- Space for a video and small (50 word) written description of the video. You can use placeholder text.
- One section with 3 Paragraphs of content (each paragraph around 100 words) with a header at the top. You can use placeholder text but please create the formatting. At the end of the 3 paragraphs please have a “Read More” Note this shouldn't be 3 separate paragraphs with three read mores - it is 3 paragraphs with one read more at the end.
- An area with the header “Search Colleges by State” that has anchor text links to all 50 states.
Top navigation:
- Home
- States – with a subnav dropdown that includes all 50 US states.
- Programs – with a subnav dropdown that includes program titles (list below)
- Degrees - with a subnav dropdown that includes 5 degree levels (list below)
- Accreditation – no subnav
- Rankings – no subnav
- Resources – no subnav
Footer
- Link to about us, privacy, and a copyright www.url.com
Programs List for sub navigation
Accounting
Art
Bible
Business
Criminal Justice
Design
Engineering
English
Law
LPN to RN
Management
Math
MBA
MPH
Medical Assisting
Military
Nursing
Occupational Therapy
Paralegal
Psychology
Pharmacy
RN to BSN
Radiology
Social Work
Sonography
Degrees list for sub navigation
Certificate
Associate
Bachelors
Masters
PhD
Thanks so much - looking forward to working with you!

```html
<!DOCTYPE html>
<html lang="en">
<head>
<meta charset="utf-8">
<title>Accredited Colleges – Home</title>
<link href="https://fonts.googleapis.com/css2?family=Lato:wght@700;900&family=Tinos:ital,wght@0,400;0,700;1,700&family=Ubuntu:ital,wght@0,300;0,400;0,500;0,700;1,400&display=swap" rel="stylesheet">
<style>
:root{
  --white:#ffffff;
  --ink:#222222;
  --nav-bg:#f2f2f2;
  --nav-text:#7a7a7a;
  --accent-red:#f05b4b;
  --accent-orange:#f06830;
  --hero-blue:#0a8ad6;
  --band-gray:#ebebea;
  --card-teal:#22b0c9;
  --card-purple:#8e8dbd;
  --video-green:#17ad7c;
  --title-teal:#2a8f9a;
  --body-text:#6d6d6d;
  --footer-bg:#363a46;
  --progress:#f07070;
  --track:#d6dde3;
}
*{margin:0;padding:0;box-sizing:border-box}
html,body{width:1200px;height:2449px;overflow:hidden}
body{font-family:'Ubuntu',sans-serif;background:var(--white);color:var(--ink);position:relative}
section,header,nav,footer{position:absolute;left:0;width:1200px}

.site-header{top:0;height:106px;background:var(--white);display:flex;align-items:center;justify-content:center}
.logo{font-family:'Lato',sans-serif;font-weight:900;font-size:46px;letter-spacing:1px;color:#111}

.main-nav{top:106px;height:49px;background:var(--nav-bg)}
.main-nav a{position:absolute;top:0;height:49px;line-height:49px;font-size:15px;font-weight:500;color:var(--nav-text);text-decoration:none;text-transform:uppercase;transform:translateX(-50%);white-space:nowrap}
.main-nav a.active{background:var(--accent-red);color:var(--white);transform:none;padding:0 16px}
.caret{display:inline-block;width:0;height:0;border-left:5px solid transparent;border-right:5px solid transparent;border-top:6px solid currentColor;margin-left:12px;vertical-align:middle}

.hero{top:155px;height:355px;background:var(--hero-blue);color:var(--white);font-family:'Tinos',serif}
.hero-word{position:absolute;left:165px;top:68px;font-size:60px;font-weight:700;letter-spacing:1px}
.hero-word .phon{font-size:32px;font-weight:400;margin-left:12px;letter-spacing:0}
.hero-pos{position:absolute;left:167px;top:130px;font-size:32px;font-style:italic;font-weight:700}
.hero-defs{position:absolute;left:165px;top:196px;font-size:19px;line-height:23.5px;list-style:none}
.hero-defs li{padding-left:24px;text-indent:-24px}
.hero-art{position:absolute;left:602px;top:50px;width:450px;height:305px;border-radius:6px;background:linear-gradient(180deg,rgba(255,255,255,.06),rgba(255,255,255,.22))}

.features{top:510px;height:374px;background:var(--band-gray)}
.card{position:absolute;top:39px;width:286px;height:304px;color:var(--white);text-align:center}
.card-ranking{left:149px;background:var(--accent-orange)}
.card-accreditation{left:455px;background:var(--card-teal)}
.card-resources{left:761px;background:var(--card-purple)}
.card-icon{width:62px;height:62px;border-radius:50%;background:rgba(255,255,255,.9);margin:26px auto 0}
.card h2{font-weight:300;font-size:35px;margin-top:14px}
.card p{font-size:13.5px;font-weight:700;line-height:16.5px;margin:10px 22px 0}

.video{top:884px;height:473px;background:var(--video-green);color:var(--white);text-align:center}
.video h2{position:absolute;left:0;width:100%;top:28px;font-weight:300;font-size:44px}
.player{position:absolute;left:367px;top:96px;width:435px;height:236px;background:var(--white)}
.player-still{position:absolute;left:0;top:0;width:435px;height:183px;background:linear-gradient(135deg,#6b6e74,#a39a93 55%,#4e5157)}
.player-controls{position:absolute;left:0;top:183px;width:435px;height:53px}
.video p{position:absolute;left:140px;width:920px;top:344px;font-size:17.5px;line-height:23.5px}

.article{top:1357px;height:476px;background:var(--white)}
.article h2{position:absolute;left:149px;top:40px;font-size:40px;font-weight:300;color:var(--title-teal)}
.article-body{position:absolute;left:149px;top:114px;width:894px;font-size:15.5px;line-height:33px;color:var(--body-text)}
.article-body p+p{margin-top:33px}
.read-more{position:absolute;left:149px;top:410px;width:121px;height:39px;line-height:39px;text-align:center;background:var(--accent-orange);color:var(--white);font-size:14px;font-weight:500;text-decoration:none}

.states{top:1833px;height:361px;background:var(--accent-red);color:var(--white)}
.states h2{position:absolute;left:0;width:100%;top:32px;text-align:center;font-weight:300;font-size:35px}
.states .rule{position:absolute;top:58px;height:2px;background:rgba(255,255,255,.75);width:222px}
.state-col{position:absolute;top:117px;list-style:none}
.state-col a{display:block;color:var(--white);font-style:italic;font-size:17.5px;line-height:33.5px}

.site-footer{top:2194px;height:255px;background:var(--footer-bg);color:var(--white);text-align:center}
.site-footer .logo{color:var(--white);position:absolute;left:0;width:100%;top:30px;font-size:40px}
.social{position:absolute;left:527px;top:102px;display:flex;gap:5px}
.social span{width:33px;height:33px;display:block}
.footer-links{position:absolute;left:0;width:100%;top:166px;font-size:15.5px}
.footer-links a{color:var(--white);text-decoration:none}
.footer-url{position:absolute;left:0;width:100%;top:200px;font-size:15px;font-style:italic}
</style>
</head>
<body>

<header class="site-header"><span class="logo">LOGO</span></header>

<nav class="main-nav">
  <a href="#" style="left:206px">Home</a>
  <a href="#" style="left:348px">States<span class="caret"></span></a>
  <a href="#" class="active" style="left:386px">Programs<span class="caret"></span></a>
  <a href="#" style="left:592px">Degrees<span class="caret"></span></a>
  <a href="#" style="left:714px">Accreditation</a>
  <a href="#" style="left:860px">Rankings</a>
  <a href="#" style="left:986px">Resources</a>
</nav>

<section class="hero">
  <h1 class="hero-word">ac·cred·it·ed<span class="phon">[uh-kred-i-tid]</span></h1>
  <div class="hero-pos">adj</div>
  <ol class="hero-defs">
    <li>1.&nbsp; officially recognized as meeting the essential requirements,<br>as of academic excellence: accredited schools.</li>
    <li>2.&nbsp; provided with official credentials, as by a government:<br>an accredited diplomatic representative.</li>
    <li>3.&nbsp; accepted as authoritative: an accredited theory.</li>
  </ol>
  <div class="hero-art" role="img" aria-label="White line illustration of academic objects: books, trophy, microscope, test tubes, globe, telescope and award ribbons"></div>
</section>

<section class="features">
  <article class="card card-ranking">
    <div class="card-icon"></div>
    <h2>Ranking</h2>
    <p>Lorem ipsum dolor sit amet, consectetur adipiscing elit. Fusce rutrum magna in nisi mattis, ut mollis lorem dictum. Morbi ac condimentum lacus. Phasellus dolor magna, rhoncus et interdum eget, tempor non sapien.</p>
  </article>
  <article class="card card-accreditation">
    <div class="card-icon"></div>
    <h2>Accreditation</h2>
    <p>Lorem ipsum dolor sit amet, consectetur adipiscing elit. Fusce rutrum magna in nisi mattis, ut mollis lorem dictum. Morbi ac condimentum lacus. Phasellus dolor magna, rhoncus et interdum eget, tempor non sapien.</p>
  </article>
  <article class="card card-resources">
    <div class="card-icon"></div>
    <h2>Resources</h2>
    <p>Lorem ipsum dolor sit amet, consectetur adipiscing elit. Fusce rutrum magna in nisi mattis, ut mollis lorem dictum. Morbi ac condimentum lacus. Phasellus dolor magna, rhoncus et interdum eget, tempor non sapien.</p>
  </article>
</section>

<section class="video">
  <h2>WATCH OUR VIDEO</h2>
  <div class="player">
    <div class="player-still" role="img" aria-label="Video still of a presenter speaking in an office"></div>
    <svg class="player-still" style="background:none" width="435" height="183" viewBox="0 0 435 183">
      <circle cx="225" cy="117" r="29" fill="rgba(255,255,255,.25)" stroke="#fff" stroke-width="4"/>
      <path d="M216 102 L240 117 L216 132 Z" fill="#fff"/>
    </svg>
    <svg class="player-controls" width="435" height="53" viewBox="0 0 435 53">
      <circle cx="29" cy="27" r="12" fill="#5f7282"/>
      <path d="M25 21 L34 27 L25 33 Z" fill="#fff"/>
      <rect x="61" y="22" width="314" height="12" fill="var(--track)"/>
      <rect x="61" y="22" width="137" height="12" fill="var(--progress)"/>
      <g stroke="#9aa8b3" stroke-width="3" fill="none">
        <path d="M396 18 L416 38 M416 18 L396 38"/>
        <path d="M396 24 V18 H402 M410 18 H416 V24 M416 32 V38 H410 M402 38 H396 V32"/>
      </g>
    </svg>
  </div>
  <p>Lorem ipsum dolor sit amet, consectetur adipiscing elit. Fusce rutrum magna in nisi mattis, ut mollis lorem dictum. Morbi ac condimentum lacus. Phasellus dolor magna, rhoncus et interdum eget, tempor non sapien. Nullam fermentum ultrices ipsum non molestie. Nunc vitae nulla ut felis ultrices mollis nec vel felis. Sed vehicula orci a orci vehicula mattis.</p>
</section>

<section class="article">
  <h2>HEADER TITLE 1</h2>
  <div class="article-body">
    <p>Lorem ipsum dolor sit amet, consectetur adipiscing elit. Donec accumsan nec ipsum a auctor. Nulla facilisi. Aliquam erat volutpat. Mauris suscipit diam a eros faucibus, non imperdiet urna porttitor. Nulla at faucibus libero. Donec congue tincid-unt volutpat.</p>
    <p>Nulla facilisi. Nulla sit amet vehicula ante. Nunc non sapien neque. In suscipit hendrerit metus id pellentesque.<br>Proin volutpat turpis et rutrum congue. Curabitur eget ipsum volutpat, mollis est in, rutrum velit. Vivamus tellus elit, lacinia ac ullamcorper in, commodo nec nibh.</p>
    <p>Pellentesque sit amet urna nec sem pulvinar pellentesque a a lorem.<br>Proin id ultrices urna. Fusce sed nisi sed augue vehicula semper a consequat nunc. Maecenas eu feugiat erat. Integer tincid-</p>
  </div>
  <a href="#" class="read-more">READMORE</a>
</section>

<section class="states">
  <span class="rule" style="left:149px"></span>
  <h2>Search Colleges by State</h2>
  <span class="rule" style="left:824px"></span>
  <ul class="state-col" style="left:167px"><li><a href="#">California</a></li><li><a href="#">Texas</a></li><li><a href="#">Illinois</a></li><li><a href="#">Virginia</a></li><li><a href="#">Massachusetts</a></li></ul>
  <ul class="state-col" style="left:322px"><li><a href="#">Kentucky</a></li><li><a href="#">Florida</a></li><li><a href="#">New Jersey</a></li><li><a href="#">Pennsylvania</a></li><li><a href="#">Alaska</a></li></ul>
  <ul class="state-col" style="left:478px"><li><a href="#">Louisiana</a></li><li><a href="#">Arizona</a></li><li><a href="#">Georgia</a></li><li><a href="#">Tennessee</a></li><li><a href="#">Colorado</a></li></ul>
  <ul class="state-col" style="left:627px"><li><a href="#">California</a></li><li><a href="#">Texas</a></li><li><a href="#">Illinois</a></li><li><a href="#">Virginia</a></li><li><a href="#">Massachusetts</a></li></ul>
  <ul class="state-col" style="left:780px"><li><a href="#">Kentucky</a></li><li><a href="#">Florida</a></li><li><a href="#">New Jersey</a></li><li><a href="#">Pennsylvania</a></li><li><a href="#">Alaska</a></li></ul>
  <ul class="state-col" style="left:937px"><li><a href="#">Louisiana</a></li><li><a href="#">Arizona</a></li><li><a href="#">Georgia</a></li><li><a href="#">Tennessee</a></li><li><a href="#">Colorado</a></li></ul>
</section>

<footer class="site-footer">
  <span class="logo">LOGO</span>
  <div class="social" aria-label="Social links">
    <span style="background:#4a6aa8"></span>
    <span style="background:#3aa2dc"></span>
    <span style="background:#d2463a"></span>
    <span style="background:#c9262e"></span>
  </div>
  <div class="footer-links"><a href="#">about us</a> &nbsp;|&nbsp; <a href="#">privacy</a> &nbsp;|&nbsp; <a href="#">copyright</a></div>
  <div class="footer-url">www.url.com</div>
</footer>

</body>
</html>
```